Business & Good Life in perfect harmony

Our company is engage in event planning & services , we have Convention center ideal for seminars, retreats,conventions, conferences or even concerts & also offers lodging facilities particularly of "ON - LINE ROOM RESERVATIONS /ACCOMMODATIONS "
Also we have Clubhouse & restobar , an elegant venue ideal for weddings, birthday celebration, parties & other memorable gatherings, as well as sports activities.
Target Market(s)
Travellers
Event Organizers
Conference / seminar Coordinators
Industry/Entity Type
Event Planning
Contact Information for Business Card
Lia B. Morendo , Sales & Operation Manager
Stonebrook Business & Convention Center Corp.
/ Stonebrook Clubhouse & Restobar
Contact #s : 082-5193068 ; 0917 4362580
Website : www. stonebrookvenue.example
Email add : stonebrook.lia.venue@mailbox.example
stonebrook.venue@postbox.example
Facebook : Stonebrook Venue
Font styles to use
Look and feel
Each slider illustrates characteristics of the customer's brand and the style your logo design should communicate.

```html
<!DOCTYPE html>
<html lang="en">
<head>
<meta charset="utf-8">
<title>Stonebrook Clubhouse &amp; Restobar — Business Card</title>
<link rel="stylesheet" href="https://fonts.googleapis.com/css2?family=Didact+Gothic&family=Noto+Sans:wght@400&display=swap">
<style>
  :root {
    --stage: #e9e7e4;
    --panel: rgba(58, 61, 66, 0.93);
    --band: rgba(96, 104, 108, 0.55);
    --rule: rgba(255, 255, 255, 0.55);
    --ink: #ffffff;
    --ink-soft: #f1f3f3;
    --photo-sky: #d8dde3;
    --photo-house: #eeeeea;
    --photo-green: #5f7d57;
    --photo-pool: #49b3b0;
    --photo-deck: #c9c3b6;
  }
  * { margin: 0; padding: 0; box-sizing: border-box; }
  html, body {
    width: 1200px; height: 899px; overflow: hidden;
    background: var(--stage);
  }
  .card {
    position: absolute; left: 75px; top: 130px;
    width: 1050px; height: 640px;
    overflow: hidden;
    box-shadow: 0 10px 30px rgba(0,0,0,0.25);
  }
  .card__photo {
    position: absolute; inset: 0;
    background:
      linear-gradient(180deg,
        var(--photo-sky) 0%,
        var(--photo-house) 28%,
        #d9d4cb 45%,
        var(--photo-green) 56%,
        var(--photo-pool) 66%,
        #3e9c9a 78%,
        var(--photo-deck) 88%,
        #8a8f7e 100%);
  }
  .card__band {
    position: absolute; top: 0; bottom: 0;
    left: 410px; width: 34px;
    background: var(--band);
  }
  .card__rule {
    position: absolute; top: 0; bottom: 0;
    left: 444px; width: 2px;
    background: var(--rule);
  }
  .card__panel {
    position: absolute; top: 0; bottom: 0;
    left: 446px; right: 0;
    background: var(--panel);
    color: var(--ink);
  }
  .venue-name {
    position: absolute; top: 62px; left: 0; right: 0;
    text-align: center;
    font-family: "Didact Gothic", sans-serif;
    font-size: 31px; line-height: 1.15;
    text-transform: uppercase;
    letter-spacing: 0.5px;
  }
  .person { position: absolute; top: 170px; left: 0; right: 0; text-align: center; }
  .person__name {
    font-family: "Didact Gothic", sans-serif;
    font-size: 36px; line-height: 1.1;
  }
  .person__role {
    font-family: "Didact Gothic", sans-serif;
    font-size: 19px; margin-top: 4px; margin-left: 80px;
  }
  .contact {
    position: absolute; left: 34px;
    font-family: "Noto Sans", sans-serif;
    color: var(--ink-soft);
    letter-spacing: 2px;
  }
  .contact--email { top: 268px; font-size: 20px; line-height: 1.35; }
  .contact--phone { top: 392px; left: 40px; font-size: 22px; line-height: 1.45; }
  .contact--phone .contact__indent { padding-left: 70px; display: block; }
  .contact--web { top: 462px; left: 36px; font-size: 21px; line-height: 1.45; }
  .contact--web .contact__indent { padding-left: 72px; display: block; }
  .tagline {
    position: absolute; bottom: 48px; left: 34px;
    font-family: "Didact Gothic", sans-serif;
    font-size: 32px; letter-spacing: -0.5px;
    text-transform: uppercase;
  }
</style>
</head>
<body>
  <div class="card">
    <div class="card__photo" role="img" aria-label="Photograph of the clubhouse building beside its swimming pool"></div>
    <div class="card__band"></div>
    <div class="card__rule"></div>
    <div class="card__panel">
      <h1 class="venue-name">Stonebrook Clubhouse<br>&amp; Restobar</h1>
      <div class="person">
        <p class="person__name">Lia B. Morendo</p>
        <p class="person__role">Sales &amp; Operation Manager</p>
      </div>
      <p class="contact contact--email">stonebrook.lia.venue@mailbox.example<br>stonebrook.venue@postbox.example</p>
      <p class="contact contact--phone">Call:  082-5193068<span class="contact__indent">0917 4362580</span></p>
      <p class="contact contact--web"><span class="contact__indent">Stonebrook Venue</span>www. stonebrookvenue.example</p>
      <p class="tagline">On - Line Room Accommodations</p>
    </div>
  </div>
</body>
</html>
```